Quibont homepage

Re-design www.quibont-example.com. Visitors are developers and CTOs. Something simple and straightforward. Need different and special landingpage.
I like this page: http://melvantry-example.io/ (service is also similar).
Logo is at http://www.quibont-example.com/quibont.svg
Be bold with content you see on www.quibont-example.com.
If you want ... make main message shorter, add links that doesn't exist, remove something etc.
Landing page should be cleaner than it is now.
Things what I want to have on page (missing on quibont-example.com):
- testimonials
- contact form (can be simple as "send us e-mail...")
Quibont supports Tavix, Brimhollow, Fenlow and Korvet. You are welcome to use logos for those databases.
CTO-s and developers/programmers
It Service

```html
<!DOCTYPE html>
<html lang="en">
<head>
<meta charset="utf-8">
<title>Quibont — Homepage</title>
<link href="https://fonts.googleapis.com/css2?family=Open+Sans:wght@300;400;600;700&family=Roboto+Mono&display=swap" rel="stylesheet">
<style>
:root{
  --brand:#1aa9d4;
  --brand-dark:#0d7fa3;
  --ink:#2b2e31;
  --muted:#8a8f94;
  --page:#ffffff;
  --night:#3b3e41;
  --night-deep:#2a2c2e;
  --terminal:#2f3133;
  --tab:#e6e8ea;
  --rule:#d9dcdf;
}
*{box-sizing:border-box;margin:0;padding:0}
html,body{width:1200px;height:4000px;overflow:hidden;background:var(--page);font-family:"Open Sans",Arial,sans-serif;color:var(--ink)}
.page{position:relative;width:1200px;height:4000px}
section,header,footer{position:absolute;left:0;width:1200px}

/* header */
.site-header{top:0;height:100px;display:flex;align-items:center;padding:0 80px}
.brand{display:flex;align-items:center;gap:14px;font-size:34px;font-weight:600;color:var(--ink)}
.brand-dot{width:30px;height:30px;border-radius:50%;background:var(--brand)}
.main-nav{margin-left:auto;display:flex;gap:40px;align-items:center;font-size:15px;letter-spacing:1px;text-transform:uppercase;color:var(--ink)}
.nav-button{background:var(--brand);color:#fff;padding:10px 30px;font-weight:600}

/* hero */
.hero{top:100px;height:360px;background:linear-gradient(100deg,#5d6b78 0%,#8ea0ad 40%,#c9d2d8 70%,#e9edf0 100%)}
.hero-copy{position:absolute;left:70px;top:110px;color:#fff;text-transform:uppercase}
.hero-copy .name{font-size:56px;font-weight:300;line-height:1;color:#fff}
.hero-copy .line{font-size:40px;font-weight:300;line-height:1.1;color:#bfe9f6}
.hero-arrows{display:flex;gap:10px;margin-top:16px}
.hero-arrows span{width:28px;height:28px;border:2px solid #fff;border-radius:50%}

/* promo band */
.promo{top:460px;height:130px;background:var(--brand);text-align:center;color:#fff}
.promo-kicker{margin-top:14px;font-size:15px;letter-spacing:3px;text-transform:uppercase}
.promo-title{font-size:40px;font-weight:300;text-transform:uppercase;line-height:1.2}
.promo-button{display:inline-block;margin-top:6px;background:#fff;color:var(--ink);font-weight:700;font-size:15px;padding:6px 40px}

/* benefits */
.benefits-head{top:590px;height:140px;text-align:center}
.section-title{font-size:54px;font-weight:300;text-transform:uppercase;margin-top:46px}
.section-lead{font-size:15px;color:var(--muted);width:420px;margin:4px auto 0;line-height:1.5}
.benefit{height:240px}
.benefit-text{position:absolute;top:50px;width:440px}
.benefit-text h3{font-size:30px;font-weight:400;margin-bottom:8px;white-space:nowrap}
.benefit-text h3 em{font-style:italic;color:var(--muted);font-weight:300}
.benefit-text p{font-size:14px;line-height:1.5;color:var(--muted)}
.benefit.text-left .benefit-text{left:340px}
.benefit.text-right .benefit-text{left:540px;text-align:right}
.benefit svg{position:absolute;top:20px;width:200px;height:200px}
.benefit.text-left svg{left:860px}
.benefit.text-right svg{left:70px}

/* install */
.install{top:1690px;height:480px;background:var(--night);color:#fff;text-align:center}
.install .section-title{margin-top:34px;font-size:50px}
.install .section-lead{color:#a9adb1}
.install-box{position:absolute;left:200px;top:170px;width:800px;height:260px;background:var(--tab);padding:14px 18px}
.tabs{display:flex;gap:6px;text-align:left}
.tab{background:#f6f7f8;color:var(--ink);font-size:15px;padding:6px 22px;border:1px solid var(--rule)}
.tab.active{background:#fff;border-bottom-color:#fff}
.terminal{background:var(--terminal);height:196px;padding:26px 28px;text-align:left;font-family:"Roboto Mono",monospace;font-size:15px;line-height:1.75;color:#fff;white-space:nowrap;overflow:hidden}

/* testimonials */
.testimonials{top:2170px;height:660px;text-align:center}
.testimonials .section-title{margin-top:30px}
.testimonials .section-lead{width:820px;font-size:13px}
.quote-mark{position:absolute;top:210px;font-size:90px;color:var(--brand);font-weight:700;line-height:1}
.quotes{position:absolute;left:130px;top:240px;width:940px;display:flex;justify-content:space-between}
.client{width:280px;display:flex;flex-direction:column;align-items:center}
.bubble{position:relative;width:240px;background:var(--night-deep);color:#fff;font-size:13px;font-weight:600;text-align:left;padding:14px 18px;line-height:1.4}
.bubble::after{content:"";position:absolute;left:50%;bottom:-14px;margin-left:-14px;border:14px solid transparent;border-bottom:0;border-top-color:var(--night-deep)}
.portrait{width:170px;height:170px;border-radius:50%;margin-top:34px;background:radial-gradient(circle at 50% 40%,#e6c3a5,#a47a5c 60%,#5f4a3c)}
.client-name{font-size:30px;font-weight:400;margin-top:14px}
.client-role{font-size:13px;color:var(--muted)}

/* location */
.find-band{top:2830px;height:70px;background:var(--night);color:#fff;text-align:center;font-size:36px;font-weight:300;line-height:70px}
.map{top:2900px;height:400px;background:linear-gradient(135deg,#d7dde0,#e9ecee 50%,#cfd8dc)}
.map-card{position:absolute;left:200px;top:150px;width:800px;height:90px;background:var(--brand);color:#fff;display:flex;align-items:center;padding:0 30px}
.map-card p{font-size:14px;line-height:1.5;font-weight:600}
.map-card .send{margin-left:auto;background:#fff;color:var(--brand);font-weight:700;padding:10px 34px;font-size:14px}
.map-card .pin{width:28px;height:36px;margin-right:18px}

/* footer */
.site-footer{top:3300px;height:700px;background:var(--night-deep);color:#fff;display:flex}
.footer-about{width:250px;background:#222426;padding:60px 40px;font-size:14px;line-height:1.7;color:#b8bcc0}
.footer-about h4{font-size:22px;color:#fff;margin-bottom:20px}
.footer-cols{display:flex;gap:70px;padding:60px 70px}
.footer-col h5{font-size:15px;font-weight:600;margin-bottom:18px}
.footer-col li{list-style:none;font-size:14px;color:#b8bcc0;line-height:2}
</style>
</head>
<body>
<div class="page">

<header class="site-header">
  <div class="brand"><span class="brand-dot"></span>Quibont</div>
  <nav class="main-nav">
    <span>Documentation</span><span>Benefits</span><span>Compare</span><span class="nav-button">Download</span>
  </nav>
</header>

<section class="hero" role="img" aria-label="Photo of a large bridge at dusk with two smartphones showing the Quibont app">
  <div class="hero-copy">
    <div class="name">Quibont</div>
    <div class="line">is related</div>
    <div class="line">to programming</div>
    <div class="hero-arrows"><span></span><span></span></div>
  </div>
</section>

<section class="promo">
  <div class="promo-kicker">Speed up building mobile app</div>
  <div class="promo-title">Free awsome program</div>
  <span class="promo-button">Download</span>
</section>

<section class="benefits-head">
  <h2 class="section-title">Benefits of Quibont</h2>
  <p class="section-lead">With Quibont you can give documentation and your data source URL and you are done.</p>
</section>

<section class="benefit text-left" style="top:730px">
  <div class="benefit-text">
    <h3>Easy to start</h3>
    <p>Quibont is lightweight and very easy to configure. That's why you can start using data in minutes.</p>
  </div>
  <svg viewBox="0 0 200 200" aria-hidden="true">
    <circle cx="100" cy="100" r="92" fill="var(--brand)"/>
    <path d="M100 100 L200 200 L200 130 Z" fill="var(--brand-dark)" opacity=".35"/>
    <path d="M74 72 A40 40 0 1 0 126 72" fill="none" stroke="#fff" stroke-width="14" stroke-linecap="round"/>
    <line x1="100" y1="50" x2="100" y2="100" stroke="#fff" stroke-width="14" stroke-linecap="round"/>
  </svg>
</section>

<section class="benefit text-right" style="top:970px">
  <div class="benefit-text">
    <h3>Less code <em>(if any...)</em></h3>
    <p>Traditional approach is to rely on the SQL connection handling and serialization. Each service needs its own layer that you must write, maintain and extend for every new client. Quibont makes this work almost completely different. We serve API.</p>
  </div>
  <svg viewBox="0 0 200 200" aria-hidden="true">
    <circle cx="100" cy="100" r="92" fill="var(--brand)"/>
    <path d="M100 100 L190 200 L200 140 Z" fill="var(--brand-dark)" opacity=".35"/>
    <rect x="48" y="56" width="104" height="86" rx="8" fill="none" stroke="#fff" stroke-width="10"/>
    <line x1="48" y1="80" x2="152" y2="80" stroke="#fff" stroke-width="8"/>
    <rect x="64" y="96" width="34" height="8" fill="#fff"/><rect x="64" y="112" width="24" height="8" fill="#fff"/>
    <circle cx="124" cy="120" r="18" fill="#fff"/>
  </svg>
</section>

<section class="benefit text-left" style="top:1210px">
  <div class="benefit-text">
    <h3>Shorter todo list</h3>
    <p>Development without effort has a list of required actions: data to be changed often, with no ending. Each time new tables arrive, the service layer must be rebuilt again.</p>
    <p>Quibont solves the problem as it reads your queries from source. It serves new data at once in a predictable way, and you can add fields later with no service release.</p>
  </div>
  <svg viewBox="0 0 200 200" aria-hidden="true">
    <circle cx="100" cy="100" r="92" fill="var(--brand)"/>
    <path d="M100 100 L200 190 L200 120 Z" fill="var(--brand-dark)" opacity=".35"/>
    <rect x="60" y="48" width="80" height="104" rx="6" fill="none" stroke="#fff" stroke-width="10"/>
    <rect x="82" y="40" width="36" height="18" rx="3" fill="#fff"/>
    <rect x="76" y="76" width="48" height="7" fill="#fff"/><rect x="76" y="96" width="48" height="7" fill="#fff"/><rect x="76" y="116" width="34" height="7" fill="#fff"/>
  </svg>
</section>

<section class="benefit text-right" style="top:1450px">
  <div class="benefit-text">
    <h3>Integration for different platforms</h3>
    <p>With API a common question is what is the format for data exchange? Quibont approach is different: data is presented as chosen and client decides which format it is. Any well known format like JSON, XML, HTML etc.</p>
  </div>
  <svg viewBox="0 0 200 200" aria-hidden="true">
    <circle cx="100" cy="100" r="92" fill="var(--brand)"/>
    <path d="M100 100 L190 200 L200 150 Z" fill="var(--brand-dark)" opacity=".35"/>
    <ellipse cx="92" cy="62" rx="42" ry="14" fill="#fff"/>
    <path d="M50 76 Q92 96 134 76 V94 Q92 114 50 94 Z" fill="#fff"/>
    <path d="M50 102 Q92 122 134 102 V120 Q92 140 50 120 Z" fill="#fff"/>
    <circle cx="138" cy="128" r="20" fill="#fff" stroke="var(--brand)" stroke-width="6"/>
  </svg>
</section>

<section class="install">
  <h2 class="section-title">Get Quibont</h2>
  <p class="section-lead">With Quibont you can give documentation and your data source URL and you are done.</p>
  <div class="install-box">
    <div class="tabs"><span class="tab active">Tarnix</span><span class="tab">Delvora</span><span class="tab">Fenrik</span><span class="tab">Tarnix</span></div>
    <div class="terminal">
      wget http://www.quibont-example.com/beta/tarnix/quibont_1.0-1_amd64.deb<br>
      apt-get install libbrimq-dev libtavixclient-dev libfenlow3-dev zpakcore-dev<br>
      libtermkit-dev &nbsp; dpkg -i quibont_1.0-1_amd64.deb<br>
      quibont
    </div>
  </div>
</section>

<section class="testimonials">
  <h2 class="section-title">Client testimonials</h2>
  <p class="section-lead">Developers and technical leads who run their services on Quibont tell how a single API layer changed their daily work, shortened release cycles and removed weeks of repeated service code from every new project they start.</p>
  <span class="quote-mark" style="left:80px">&ldquo;</span>
  <span class="quote-mark" style="left:1080px">&rdquo;</span>
  <div class="quotes">
    <div class="client">
      <p class="bubble">Setup took ten minutes and our mobile team had live data before lunch. We dropped a whole service layer.</p>
      <div class="portrait" role="img" aria-label="Portrait photo of client John Doe"></div>
      <div class="client-name">John Doe</div>
      <div class="client-role">Nortwell Cycle, CEO</div>
    </div>
    <div class="client">
      <p class="bubble">Less code to keep alive and clean formats for every client. Our developers finally build features again.</p>
      <div class="portrait" role="img" aria-label="Portrait photo of client Jane Smith"></div>
      <div class="client-name">Jane Smith</div>
      <div class="client-role">Nortwell Cycle, CEO</div>
    </div>
    <div class="client">
      <p class="bubble">We connected three databases in one afternoon. The API just works and support answers right away.</p>
      <div class="portrait" role="img" aria-label="Portrait photo of client Jane Smith"></div>
      <div class="client-name">Jane Smith</div>
      <div class="client-role">Nortwell Cycle, CEO</div>
    </div>
  </div>
</section>

<section class="find-band">FIND US</section>

<section class="map" role="img" aria-label="Street map around the Quibont office">
  <div class="map-card">
    <svg class="pin" viewBox="0 0 28 36" aria-hidden="true"><path d="M14 0 A14 14 0 0 1 28 14 C28 24 14 36 14 36 C14 36 0 24 0 14 A14 14 0 0 1 14 0 Z" fill="#fff"/><circle cx="14" cy="14" r="5" fill="var(--brand)"/></svg>
    <p>Headquarters<br>125 Larkmoor Street, Suite 4, Harbury 20410<br>Tel 555-0142</p>
    <span class="send">Send us e-mail</span>
  </div>
</section>

<footer class="site-footer">
  <div class="footer-about">
    <h4>Quibont</h4>
    <p>A simple, fast API layer for your data. Built for developers and CTOs who want less code, fewer services and clean formats for every client.</p>
  </div>
  <div class="footer-cols">
    <div class="footer-col"><h5>About Us</h5><ul><li>Dashboard</li><li>Host</li><li>Graphs</li><li>Journal</li><li>Store</li></ul></div>
    <div class="footer-col"><h5>Categories</h5><ul><li>Web Designs</li><li>Photography</li><li>Digital Art</li><li>Vector Art</li><li>Tutorials</li></ul></div>
    <div class="footer-col"><h5>Networks</h5><ul><li>Other Sites</li><li>Insight</li><li>Planning</li><li>Production</li><li>Store</li></ul></div>
    <div class="footer-col"><h5>Follow Us</h5><ul><li>Chatterly</li><li>Pinwave</li><li>Linkroom</li><li>Myhaven</li><li>Clipstream</li></ul></div>
  </div>
</footer>

</div>
</body>
</html>
```